A home-based beauty salon needs a website

Creation of an aesthetically pleasing and user-friendly website, crucial for showcasing our products, services and driving customer engagement/online bookings.

Focusing on key elements:
- mobile compatibility (fast loading on mobile)
- accessibility
- well-planned information architecture
- effective navigation
- simple forms (Contact Us)
- blog
- online store (e.g. shopify) to sell beauty products
- newsletter subscription
- online booking: integrate with existing engine = Fresha
- easy ongoing maintenance

Objective of website:
- Build online brand presence: classy, aesthetic and professional
- Drive online bookings
- Drive online sales

Services offered:
- Laser Hair Removal
- Chemical Peels
- Advanced Skin Treatments
- LED Light Therapy
- Teeth Whitening

Inspiration:
Ideal layout and function: https://velinorskin.ca/
Innovative and sleek design: https://www.studiotavi.sk/

Instagram: https://www.pictogrove.com/bramelskin_official/

Colour preferences: Black, White, and if possible Tropical Rainforest Palm Leave greens to match our feature-wall in the clinic room (see uploaded files for example behind our business logo). Open to seeing light pastel colours as well.

Copy: to be provided post design-phase
Images: of the clinic and our machines can be provided during design-phase
Font style: fancy and light to match the logo

Sections:
Home, About, Spa (Hydro-dermabrasion, LED Light Therapy, Peels, Facials, Signature Packages), Medical (Laser Hair Removal, Chemical Peels, Teeth Whitening), Contact, Blog

Industry/Entity Type

Beauty and Skincare Industry

Coding

Coded - Design and coding required

Number of Pages Required

5+ page

Colors

Designer to choose colors to be used in the design.

Requirements
Must have
• Integration with Shopify or similar, Integration with Afterpay or Zip Pay, Newsletter subscription pop-up or similar, Map to visualise location and make it easy for customers to find us, Integration with our Fresha booking engine, Integration with Instagram or Gallery under each service offering to present before vs after images of treatments to support the Consideration process
Nice to have
• (1) Contact Us Page: form + visual navigation of how to get to the clinic to make it easy to find us. (2) Online Store integration with Shopify. (3) Integrate Gallery or select Instagram pictures that match the service offered to help customers see potential results when selecting services. e.g. Teeth Whitening before and after on the Teeth Whitening service page. (4) Integrate Zip Pay or Afterpay next to product/service offers making it easy to understand potential repayments . (5)

```html
<!DOCTYPE html>
<html lang="en">
<head>
<meta charset="utf-8">
<title>Bramel Beauty Salon</title>
<meta name="viewport" content="width=1200">
<link rel="stylesheet" href="https://fonts.googleapis.com/css2?family=Playfair+Display+SC:wght@700;900&family=Playfair+Display:wght@700&family=Poppins:wght@400;500;600&display=swap">
<style>
:root{
  --peach:#fcd5bf;
  --peach-deep:#f6c2a6;
  --ink:#161616;
  --paper:#f1f0ef;
  --white:#ffffff;
  --footer:#262626;
  --muted:#3a3a3a;
}
*{box-sizing:border-box;margin:0;padding:0}
html,body{width:1200px;height:5085px;overflow:hidden}
body{position:relative;font-family:"Poppins",sans-serif;color:var(--ink);background:var(--white)}
section,header,footer{position:absolute;left:0;width:1200px;overflow:hidden}
.abs{position:absolute}
.display{font-family:"Playfair Display SC",serif;font-weight:700;letter-spacing:-0.5px}
.section-title{position:absolute;left:0;width:1200px;text-align:center;font-family:"Playfair Display SC",serif;font-weight:700;font-size:44px;line-height:1}
.btn{position:absolute;background:var(--ink);color:var(--white);font-family:"Poppins",sans-serif;font-weight:600;font-size:15px;display:flex;align-items:center;justify-content:center;text-transform:uppercase}
.photo{position:absolute;overflow:hidden}

/* header + hero */
.hero{top:0;height:691px;background:var(--white)}
.brand{position:absolute;left:174px;top:40px;display:flex;align-items:center;gap:12px}
.brand-dot{width:22px;height:22px;border-radius:50%;background:var(--ink)}
.brand-name{font-family:"Playfair Display",serif;font-weight:700;font-size:34px;color:var(--ink)}
.order-line{position:absolute;right:175px;top:22px;font-size:14px;font-weight:500;display:flex;gap:6px;align-items:center}
.nav{position:absolute;left:539px;top:68px;display:flex;gap:18px;font-size:13px;font-weight:500}
.nav-icons{position:absolute;left:952px;top:62px;display:flex;gap:6px}
.nav-icons span{width:32px;height:32px;border:2px solid var(--ink);border-radius:50%;display:flex;align-items:center;justify-content:center}
.hero-title{position:absolute;left:170px;top:252px;font-size:112px;line-height:1;font-weight:900}
.hero-sub{position:absolute;left:174px;top:398px;font-size:36px;font-weight:600}
.hero-arch{position:absolute;left:690px;top:250px;width:278px;height:441px;background:var(--peach);border-radius:139px 139px 0 0}

/* services offered */
.services{top:691px;height:620px;background:transparent}
.services-band{position:absolute;left:0;top:0;width:1200px;height:520px;background:var(--peach)}
.service-card{position:absolute;top:174px;width:226px;height:330px;border:2px solid var(--ink);border-radius:113px;background:var(--white)}
.service-card.is-active{border-color:var(--peach-deep);border-width:4px}
.service-card .photo{left:8px;top:8px;width:206px;height:206px;border-radius:50%;border:2px solid var(--ink)}
.service-card h3{position:absolute;left:0;top:228px;width:100%;text-align:center;font-size:19px;font-weight:500;line-height:26px;text-transform:uppercase}
.chev{position:absolute;left:50%;bottom:-24px;margin-left:-24px;width:48px;height:48px;border-radius:50%;background:var(--ink);border:3px solid var(--white);display:flex;align-items:center;justify-content:center}

/* about */
.about{top:1253px;height:757px;background:var(--paper)}
.about h2{position:absolute;left:174px;top:174px;font-size:44px}
.about p{position:absolute;left:174px;top:250px;width:440px;font-size:12.5px;line-height:22.6px;text-align:justify}
.features{position:absolute;left:174px;top:418px;width:460px;display:grid;grid-template-columns:128px 166px 150px;row-gap:22px}
.feature{display:flex;align-items:center;gap:8px;font-size:14px;line-height:15px}
.feature i{width:44px;height:44px;border:2px solid var(--ink);border-radius:50%;display:flex;align-items:center;justify-content:center;flex:none}
.about .photo{border-radius:24px}

/* spa */
.spa{top:2010px;height:823px;background:var(--peach)}
.spa-card{position:absolute;text-align:center}
.spa-card h3{font-size:21px;font-weight:500;white-space:nowrap;text-transform:uppercase;margin-top:18px}
.spa-card p{font-size:14px;margin-top:6px}
.dots{position:absolute;top:742px;left:0;width:1200px;display:flex;justify-content:center;align-items:center;gap:16px}
.dots b{width:6px;height:6px;border-radius:50%;background:var(--ink)}
.dots b.on{width:26px;height:26px;background:none;border:2px solid var(--ink);position:relative}
.dots b.on::after{content:"";position:absolute;left:7px;top:7px;width:8px;height:8px;border-radius:50%;background:var(--ink)}

/* products */
.products{top:2833px;height:606px;background:var(--paper)}
.product{position:absolute;top:169px;width:272px;text-align:center}
.product .photo{position:relative;width:272px;height:285px;border:2px solid var(--muted)}
.stars{font-size:15px;margin-top:18px;letter-spacing:2px}
.product h3{font-size:19px;font-weight:400;margin-top:4px}
.product .price{font-size:16px;margin-top:4px}
.arrow{position:absolute;top:300px}

/* medical */
.medical{top:3439px;height:515px;background:var(--peach)}
.med-circle{position:absolute;top:168px;width:276px;height:276px;border-radius:50%;border:3px solid var(--ink);overflow:hidden}
.med-circle .photo{inset:0;width:100%;height:100%}
.med-circle h3{position:absolute;left:0;width:100%;top:200px;text-align:center;color:var(--white);font-size:21px;font-weight:600;line-height:24px;text-transform:uppercase}

/* blog */
.blog{top:3954px;height:685px;background:var(--white)}
.post{position:absolute;top:166px;width:272px}
.post .photo{position:relative;width:272px;height:227px}
.post time{display:block;font-size:11.5px;margin-top:23px}
.post h3{font-size:14.5px;font-weight:500;line-height:24px;margin-top:2px}
.post p{font-size:11.5px;line-height:18px;margin-top:6px;text-align:justify}
.post .btn{position:relative;width:120px;height:43px;margin-top:24px}

/* footer */
.footer{top:4639px;height:446px;background:var(--footer);color:var(--white)}
.footer-brand{position:absolute;left:174px;top:150px;display:flex;align-items:center;gap:14px}
.footer-brand .brand-dot{background:var(--white);width:30px;height:30px}
.footer-brand .brand-name{color:var(--white);font-size:48px}
.footer h4{position:absolute;font-family:"Playfair Display SC",serif;font-weight:700;font-size:20px;letter-spacing:0.3px}
.footer-links{position:absolute;left:442px;top:138px;list-style:none;font-size:13px;font-weight:500;line-height:29px}
.email{position:absolute;left:681px;top:132px;width:345px;height:40px;border:2px solid var(--white);font-size:13px;padding:0 9px;display:flex;align-items:center}
.subscribe{position:absolute;left:681px;top:187px;width:103px;height:40px;background:var(--white);color:var(--ink);font-size:13px;font-weight:500;display:flex;align-items:center;justify-content:center}
.pay{position:absolute;left:683px;top:296px;display:flex;gap:6px}
.pay span{width:42px;height:25px;border-radius:3px;background:var(--white)}
.pay span:nth-child(3){background:#f1c9a8}
.footer-rule{position:absolute;left:174px;top:375px;width:852px;height:1px;background:#8a8a8a}
.copyright{position:absolute;left:0;top:403px;width:1200px;text-align:center;font-size:11.5px}
</style>
</head>
<body>

<header class="hero">
  <div class="brand"><span class="brand-dot"></span><span class="brand-name">Bramel</span></div>
  <div class="order-line">
    <svg width="14" height="14" viewBox="0 0 24 24"><path d="M6.6 10.8a15.1 15.1 0 0 0 6.6 6.6l2.2-2.2a1 1 0 0 1 1-.25 11.4 11.4 0 0 0 3.6.57 1 1 0 0 1 1 1V20a1 1 0 0 1-1 1A17 17 0 0 1 3 4a1 1 0 0 1 1-1h3.5a1 1 0 0 1 1 1c0 1.25.2 2.45.57 3.57a1 1 0 0 1-.25 1z" fill="#161616"/></svg>
    ORDERS : +00 24680 1357
  </div>
  <nav class="nav"><span>HOME</span><span>ABOUT</span><span>SPA</span><span>MEDICAL</span><span>CONTACT</span><span>BLOG</span></nav>
  <div class="nav-icons">
    <span><svg width="16" height="16" viewBox="0 0 24 24" fill="none" stroke="#161616" stroke-width="2"><path d="M3 4h3l2.5 11h10l2-8H7"/><circle cx="10" cy="19" r="1.5"/><circle cx="17" cy="19" r="1.5"/></svg></span>
    <span><svg width="16" height="16" viewBox="0 0 24 24" fill="none" stroke="#161616" stroke-width="2.4"><circle cx="10.5" cy="10.5" r="6.5"/><path d="M15.5 15.5L21 21"/></svg></span>
  </div>
  <div class="hero-arch"></div>
  <div class="photo" role="img" aria-label="Portrait of a model with glowing skin beside a dried flower stem" style="left:640px;top:118px;width:480px;height:573px;background:radial-gradient(ellipse at 45% 40%,#efcdb6 0%,#e8bfa4 45%,rgba(252,213,191,0) 72%)"></div>
  <h1 class="hero-title display">BRAMEL</h1>
  <div class="hero-sub">Beauty Salon</div>
  <a class="btn" style="left:174px;top:480px;width:134px;height:45px">Contact Us</a>
</header>

<section class="services">
  <div class="services-band"></div>
  <svg class="abs" style="left:0;top:519px" width="1200" height="80" viewBox="0 0 1200 80" preserveAspectRatio="none"><path d="M0 0H1200V10Q600 100 0 40Z" fill="#fcd5bf"/></svg>
  <h2 class="section-title" style="top:68px">SERVICES OFFERED</h2>
  <article class="service-card" style="left:115px">
    <div class="photo" role="img" aria-label="Client receiving laser hair removal treatment" style="background:linear-gradient(160deg,#e8ddd6,#c9a896)"></div>
    <h3>Laser Hair<br>Removal</h3>
    <span class="chev"><svg width="18" height="18" viewBox="0 0 24 24" fill="none" stroke="#fff" stroke-width="3"><path d="M6 9l6 6 6-6"/></svg></span>
  </article>
  <article class="service-card is-active" style="left:363px">
    <div class="photo" role="img" aria-label="Chemical peel being applied to a client's skin" style="background:linear-gradient(160deg,#dfe3e6,#d7a98b)"></div>
    <h3>Chemical<br>Peels</h3>
    <span class="chev"><svg width="18" height="18" viewBox="0 0 24 24" fill="none" stroke="#fff" stroke-width="3"><path d="M6 9l6 6 6-6"/></svg></span>
  </article>
  <article class="service-card" style="left:611px">
    <div class="photo" role="img" aria-label="Advanced skin treatment with a face mask" style="background:linear-gradient(160deg,#d9dbe0,#9a6f5f)"></div>
    <h3>Advanced Skin<br>Treatments</h3>
    <span class="chev"><svg width="18" height="18" viewBox="0 0 24 24" fill="none" stroke="#fff" stroke-width="3"><path d="M6 9l6 6 6-6"/></svg></span>
  </article>
  <article class="service-card" style="left:859px">
    <div class="photo" role="img" aria-label="LED light therapy mask glowing purple" style="background:radial-gradient(circle at 50% 45%,#c545ff,#6a10c8 55%,#2a0666)"></div>
    <h3>LED Light<br>Therapy</h3>
    <span class="chev"><svg width="18" height="18" viewBox="0 0 24 24" fill="none" stroke="#fff" stroke-width="3"><path d="M6 9l6 6 6-6"/></svg></span>
  </article>
</section>

<section class="about" style="z-index:-1">
  <h2 class="display">ABOUT US</h2>
  <p>Nibh sit amet commodo nulla facilisi. Aliquet porttitor lacus luctus accumsan tortor posuere. Volutpat diam ut venenatis tellus in metus vulputate eu scelerisque. Feugiat scelerisque varius morbi enim nunc faucibus. Malesuada fames ac turpis egestas maecenas pharetra convallis posuere morbi. Tincidunt arcu non sodales non consectetur a erat nam at lectus.</p>
  <div class="features">
    <div class="feature"><i><svg width="20" height="20" viewBox="0 0 24 24" fill="none" stroke="#161616" stroke-width="1.6"><path d="M12 20C5 16 4 9 5 5c4 0 11 1 14 6-2 5-5 8-7 9z"/><path d="M12 20V9"/></svg></i>Organic</div>
    <div class="feature"><i><svg width="20" height="20" viewBox="0 0 24 24" fill="none" stroke="#161616" stroke-width="1.6"><circle cx="12" cy="12" r="7"/><path d="M8 12l3 3 5-6"/></svg></i>Sulfate-Free</div>
    <div class="feature"><i><svg width="20" height="20" viewBox="0 0 24 24" fill="#161616"><path d="M12 20c-5-3-7-8-6-13 4 1 6 5 6 9 0-4 2-8 6-9 1 5-1 10-6 13z"/></svg></i>100% Vegan</div>
    <div class="feature"><i><svg width="20" height="20" viewBox="0 0 24 24" fill="none" stroke="#161616" stroke-width="1.6"><circle cx="12" cy="12" r="7"/><path d="M7 17L17 7"/></svg></i>Cruelty<br>Free</div>
    <div class="feature"><i><svg width="20" height="20" viewBox="0 0 24 24" fill="none" stroke="#161616" stroke-width="1.6"><path d="M12 3s6 7 6 11a6 6 0 0 1-12 0c0-4 6-11 6-11z"/></svg></i>Paraben<br>Free</div>
    <div class="feature"><i><svg width="20" height="20" viewBox="0 0 24 24" fill="none" stroke="#161616" stroke-width="1.6"><path d="M10 3h4M11 3v6l-5 10h12l-5-10V3"/></svg></i>Lab-Tested</div>
  </div>
  <a class="btn" style="left:174px;top:577px;width:119px;height:45px">Shop Now</a>
  <div class="photo" role="img" aria-label="Close-up of a client receiving a gloved facial treatment" style="left:647px;top:139px;width:233px;height:359px;background:linear-gradient(170deg,#d7c3b8,#9c7665 55%,#2d2d33)"></div>
  <div class="photo" role="img" aria-label="Relaxed client with a white face mask surrounded by flowers" style="left:894px;top:139px;width:235px;height:217px;background:linear-gradient(160deg,#f3e6e0,#e7b9a7 55%,#8f5a47)"></div>
  <div class="photo" role="img" aria-label="Client wearing protective glasses during teeth whitening" style="left:744px;top:372px;width:385px;height:300px;background:linear-gradient(140deg,#f0ece9,#c99a84 50%,#3f7fd8)"></div>
</section>

<section class="spa">
  <h2 class="section-title" style="top:76px">SPA SERVICES</h2>
  <article class="spa-card" style="left:0;top:227px;width:251px">
    <div class="photo" role="img" aria-label="Hydro-dermabrasion device on a client's face" style="position:relative;width:251px;height:373px;background:linear-gradient(160deg,#7a6a66,#c29a86 55%,#3b3230)"></div>
    <h3 style="margin-left:-40px;margin-right:20px">Hydro-Dermabrasion</h3>
    <p>Nibh sit amet commodo</p>
  </article>
  <article class="spa-card" style="left:288px;top:183px;width:294px">
    <div class="photo" role="img" aria-label="Client lying under an LED light therapy panel" style="position:relative;width:294px;height:373px;background:radial-gradient(ellipse at 50% 55%,#5aa8ff,#1446d6 45%,#0a1a55 80%)"></div>
    <h3>LED Light Therapy</h3>
    <p>Nibh sit amet commodo</p>
  </article>
  <article class="spa-card" style="left:620px;top:227px;width:292px">
    <div class="photo" role="img" aria-label="Therapist applying a peel under a magnifying lamp" style="position:relative;width:292px;height:373px;background:linear-gradient(170deg,#f4f2f0,#e4d8cf 50%,#c6a593)"></div>
    <h3>Peels</h3>
    <p>Nibh sit amet commodo</p>
  </article>
  <article class="spa-card" style="left:950px;top:227px;width:292px">
    <div class="photo" role="img" aria-label="Client with a white facial mask" style="position:relative;width:292px;height:373px;background:linear-gradient(160deg,#cfcfd4,#f1f1f3 55%,#a9a9b2)"></div>
    <h3>Facials</h3>
    <p>Nibh sit amet commodo</p>
  </article>
  <div class="dots"><b></b><b></b><b class="on"></b><b></b><b></b></div>
</section>

<section class="products">
  <h2 class="section-title" style="top:78px">OUR PRODUCTS</h2>
  <svg class="arrow" style="left:68px" width="30" height="60" viewBox="0 0 30 60" fill="none" stroke="#161616" stroke-width="2.4"><path d="M26 4L4 30l22 26"/></svg>
  <svg class="arrow" style="left:1096px" width="30" height="60" viewBox="0 0 30 60" fill="none" stroke="#161616" stroke-width="2.4"><path d="M4 4l22 26L4 56"/></svg>
  <article class="product" style="left:172px">
    <div class="photo" role="img" aria-label="Hand holding a jar of skin cream" style="background:linear-gradient(160deg,#d6d6d6,#b9b6b4 50%,#e7e3df)"></div>
    <div class="stars">★★★★☆</div>
    <h3>Nibh Sit Amet Nulla</h3>
    <div class="price">$18.00–$30.00</div>
  </article>
  <article class="product" style="left:464px">
    <div class="photo" role="img" aria-label="Row of skincare tubes and serum bottles" style="background:linear-gradient(180deg,#f4f4f4,#e9e5e2 55%,#8a5b4a)"></div>
    <div class="stars">★★★★☆</div>
    <h3>Nibh Sit Amet Nulla</h3>
    <div class="price">$18.00–$30.00</div>
  </article>
  <article class="product" style="left:756px">
    <div class="photo" role="img" aria-label="Skincare products with an application brush" style="background:linear-gradient(160deg,#f2f0ef,#e7d3cb 55%,#c2554f)"></div>
    <div class="stars">★★★★☆</div>
    <h3>Nibh Sit Amet Nulla</h3>
    <div class="price">$18.00–$30.00</div>
  </article>
</section>

<section class="medical">
  <h2 class="section-title" style="top:76px">MEDICAL SERVICES</h2>
  <article class="med-circle" style="left:174px">
    <div class="photo" role="img" aria-label="Client receiving laser hair removal on the arm" style="background:linear-gradient(180deg,#d8dde0 0%,#a8a29f 45%,#1c1c1c 100%)"></div>
    <h3>Laser Hair<br>Removal</h3>
  </article>
  <article class="med-circle" style="left:462px">
    <div class="photo" role="img" aria-label="Client wearing a black peel-off mask" style="background:linear-gradient(180deg,#e3d6cf 0%,#7a5a4d 45%,#141414 100%)"></div>
    <h3>Chemical<br>Peels</h3>
  </article>
  <article class="med-circle" style="left:750px">
    <div class="photo" role="img" aria-label="Client with orange glasses during teeth whitening" style="background:linear-gradient(180deg,#eef0f4 0%,#e0905a 45%,#1c1c1c 100%)"></div>
    <h3>Teeth<br>Whitening</h3>
  </article>
</section>

<section class="blog">
  <h2 class="section-title" style="top:80px">OUR LATEST BLOG</h2>
  <article class="post" style="left:172px">
    <div class="photo" role="img" aria-label="Woman receiving laser treatment on the leg" style="background:linear-gradient(160deg,#d9d6d4,#f0e6e2 50%,#b88e7b)"></div>
    <time>28 SEPTEMBER, 2023</time>
    <h3>The Benefits Of Relaxing Massage<br>&amp; Hot Water Bath</h3>
    <p>Adipiscing bibendum est ultricies integer quis. Iaculis nunc sed augue lacus viverra vitae nunc sed.</p>
    <a class="btn">Read More</a>
  </article>
  <article class="post" style="left:464px">
    <div class="photo" role="img" aria-label="Therapist brushing a white mask onto a client's face" style="background:linear-gradient(160deg,#e7b9c0,#f3e9e4 50%,#4f8fd1)"></div>
    <time>28 SEPTEMBER, 2023</time>
    <h3>The Benefits Of Relaxing Massage<br>&amp; Hot Water Bath</h3>
    <p>Adipiscing bibendum est ultricies integer quis. Iaculis nunc sed augue lacus viverra vitae nunc sed.</p>
    <a class="btn">Read More</a>
  </article>
  <article class="post" style="left:756px">
    <div class="photo" role="img" aria-label="Smiling patient at a dental whitening appointment" style="background:linear-gradient(160deg,#6a3b2c,#c9856a 50%,#e9e7ea)"></div>
    <time>28 SEPTEMBER, 2023</time>
    <h3>The Benefits Of Relaxing Massage<br>&amp; Hot Water Bath</h3>
    <p>Adipiscing bibendum est ultricies integer quis. Iaculis nunc sed augue lacus viverra vitae nunc sed.</p>
    <a class="btn">Read More</a>
  </article>
</section>

<footer class="footer">
  <div class="footer-brand"><span class="brand-dot"></span><span class="brand-name">Bramel</span></div>
  <h4 style="left:442px;top:82px">INFORMATION</h4>
  <ul class="footer-links"><li>HOME</li><li>ABOUT</li><li>SPA</li><li>MEDICAL</li><li>CONTACT</li><li>BLOG</li></ul>
  <h4 style="left:683px;top:82px">NEWSLETTER SUBSCRIPTION</h4>
  <div class="email">EMAIL ID</div>
  <div class="subscribe">SUBSCRIBE</div>
  <h4 style="left:683px;top:254px">ACCEPTED PAYMENTS:</h4>
  <div class="pay" aria-label="Accepted payment methods"><span></span><span></span><span></span><span></span></div>
  <div class="footer-rule"></div>
  <div class="copyright">Copyrights @ 2023 Bramel Beauty. All Rights Reserved.</div>
</footer>

</body>
</html>
```